trading data display webpage

We have build a rough wireframe of the two webpages that we want to display .The two wireframes are attached as a pdf document.
there will be login page. after login , the user will see the index page. that is the first page of the wireframe.

what we are displaying is essentially spread data. we are taking the difference in prices are two places and displaying the data. some calculations are done and is shown in the grid.

below the grid we show the behaviour on a graph. we will use bubble chart. I did not find a sample, hence have thrown in a placeholder.

this is time series data ( changes daily) and hence we need to check the behaviour.

the second wire frame shows how the user will choose the source price points and the destination price points.
we are talking here of natural gas prices hence the reference to source prices and destination prices.

you need to design the page/ pages such that the end-user loves it and is easy to use. the intent here is easy to use and easy to understand.
this will be responsive webpage since the end user will check it out on a tablet or a smartphone.

so if possible tell us how the navigation bar, the button bar, etc should fall when the screen size decreases.

I have uploaded 2 files. one is the wireframe ( pdf document) and second is the logo file.

please also let us know where to place the logo.

Target Market(s)

the target market is traders and data analyst

Industry/Entity Type

Build

Colors

Designer to choose colors to be used in the design.

Requirements
Must have
• 1. design for the web.
2. but think how the design will look when the screen size decreases.
3. tell if possible what screen components to keep and what to hide.

```html
<!DOCTYPE html>
<html lang="en">
<head>
<meta charset="utf-8">
<title>Methara — Spread Dashboard</title>
<link href="https://fonts.googleapis.com/css2?family=Open+Sans:wght@400;600;700&display=swap" rel="stylesheet">
<style>
:root{
  --sky-top:#7a4a1c;
  --sky-mid:#c98a3a;
  --sky-glow:#f0c070;
  --field:#a8773e;
  --ground:#1c1c1c;
  --frame-edge:#6d6d6d;
  --frame-black:#050505;
  --panel-light:#e6e6e6;
  --panel-mid:#b9b9b9;
  --cell-white:#ffffff;
  --cell-grey:#e3e3e3;
  --head-grey:#c9c9c9;
  --line:#1a1a1a;
  --ink:#222222;
  --tab-red:#e0322a;
  --olive:#6b7a2e;
  --orange:#e2952a;
  --slate:#3f5670;
  --navy:#1f2d3d;
  --purple:#7a56a0;
  --brown:#5a2f2f;
  --pill:rgba(240,214,170,.8);
}
*{box-sizing:border-box;margin:0;padding:0}
html,body{width:1200px;height:1172px;overflow:hidden}
body{font-family:"Open Sans",Arial,sans-serif;color:var(--ink);background:var(--ground);position:relative}

.hero-photo{position:absolute;left:0;top:0;width:1200px;height:965px;
  background:
   radial-gradient(circle at 450px 65px,#fff6d8 0 48px,rgba(255,220,150,.6) 70px,rgba(0,0,0,0) 220px),
   linear-gradient(180deg,var(--sky-top) 0,var(--sky-mid) 160px,var(--sky-glow) 340px,#8a6a4a 470px,#5e5a5a 540px,var(--field) 600px,#c49456 780px,#8d6234 965px);}
.ground-band{position:absolute;left:0;top:965px;width:1200px;height:207px;background:linear-gradient(180deg,#2a2a2a,#151515)}

.brand{position:absolute;left:47px;top:70px;display:flex;align-items:center;gap:10px}
.brand-dot{width:34px;height:34px;border-radius:50%;background:#f28c1e}
.brand-name{font-size:34px;font-weight:700;color:#ffffff}

.top-nav{position:absolute;left:787px;top:32px;width:386px;height:43px;border-radius:14px;background:var(--pill);
  display:flex;align-items:center;padding-left:10px;gap:9px;font-size:20px;color:#1b1b1b}
.top-nav .sep{color:#333}
.social{display:flex;gap:5px;margin-left:6px}
.social span{width:26px;height:26px;border-radius:4px;background:#3a5a98}
.social span:nth-child(2){background:#35a6d8}
.social span:nth-child(3){background:#d9a23a}

.region-tabs{position:absolute;left:122px;top:416px;display:flex;gap:4px;z-index:2}
.region-tab{width:140px;height:36px;background:linear-gradient(180deg,#2b2b2b,#000);color:#fff;
  border-top:2px solid #8a8a8a;border-radius:12px 22px 0 0;font-size:16px;display:flex;align-items:center;padding-left:28px;line-height:1.05}
.region-tab.small{font-size:12px}
.region-tab.active{color:var(--tab-red)}
.region-tab::before{content:">";margin-right:8px;color:inherit}

.dashboard-frame{position:absolute;left:109px;top:437px;width:978px;height:670px;border-radius:22px;
  background:var(--frame-black);border:9px solid var(--frame-edge)}
.grid-panel{position:absolute;left:139px;top:461px;width:918px;height:366px;
  background:linear-gradient(90deg,#8f8f8f,var(--panel-light) 18%,#f4f4f4 50%,var(--panel-light) 82%,#8f8f8f)}
.controls{position:absolute;top:28px;left:0;width:100%;height:24px}
.select{position:absolute;height:24px;border:1px solid #333;background:#fff;font-size:14px;padding-left:7px;display:flex;align-items:center}
.select .arrow{position:absolute;right:2px;top:2px;width:18px;height:18px;border:1px solid #333;border-radius:3px;background:#eee;font-size:8px;line-height:8px;text-align:center;padding-top:1px}
.select.source{left:32px;width:141px}
.select.dest{left:716px;width:168px}
.toggle{position:absolute;display:flex;height:24px;border:1px solid #333;background:#f5f5f5;font-size:11px}
.toggle span{display:flex;align-items:center;justify-content:center;border-right:1px solid #333}
.toggle span:last-child{border-right:0}
.toggle.days{left:260px;width:197px;border-radius:0 12px 12px 0}
.toggle.days span{width:60px}.toggle.days span:last-child{width:75px}
.toggle.period{left:564px;width:142px;height:18px;top:3px;font-size:8px}
.toggle.period span{width:71px}

.spread-table{position:absolute;left:29px;top:70px;width:860px;border-collapse:collapse;font-size:15px}
.spread-table th,.spread-table td{border:2px solid var(--line);height:43px;text-align:left;padding-left:3px;font-weight:400}
.spread-table th{background:var(--head-grey);font-size:14px}
.spread-table tr:nth-child(odd) td{background:var(--cell-grey)}
.spread-table tr:nth-child(even) td{background:var(--cell-white)}

.chart-panel{position:absolute;left:139px;top:829px;width:918px;height:218px;
  background:linear-gradient(90deg,#8f8f8f,var(--panel-light) 18%,#f4f4f4 50%,var(--panel-light) 82%,#8f8f8f)}
.chart-card{position:absolute;top:16px;background:#fff;box-shadow:0 14px 10px -8px rgba(0,0,0,.35)}
.chart-card.bars{left:26px;width:395px;height:175px}
.chart-card.pie{left:490px;width:396px;height:178px}
.chart-card svg{display:block}

.footer{position:absolute;top:1133px;left:0;width:1200px;text-align:center;font-size:13px;color:#fff;display:flex;justify-content:center;align-items:center;gap:14px}
.footer .brand-mini{font-weight:700;font-size:15px}
</style>
</head>
<body>
<div class="hero-photo" role="img" aria-label="Oil pump jacks silhouetted against a sunset over open fields"></div>
<div class="ground-band"></div>

<div class="brand"><span class="brand-dot"></span><span class="brand-name">Methara</span></div>

<nav class="top-nav">
  <span>Home</span><span class="sep">|</span><span>Index</span><span class="sep">|</span><span>Contact</span>
  <span class="social"><span></span><span></span><span></span></span>
</nav>

<div class="region-tabs">
  <div class="region-tab active">East</div>
  <div class="region-tab">Central</div>
  <div class="region-tab">West</div>
  <div class="region-tab small">Valuable<br>Information</div>
  <div class="region-tab small">Important<br>Information</div>
</div>

<div class="dashboard-frame"></div>

<section class="grid-panel">
  <div class="controls">
    <div class="select source">Source Indices<span class="arrow">▲<br>▼</span></div>
    <div class="toggle days"><span>5 days</span><span>7 days</span><span>18 days</span></div>
    <div class="toggle period"><span>Month</span><span>Year</span></div>
    <div class="select dest">Destination Indices<span class="arrow">▲<br>▼</span></div>
  </div>
  <table class="spread-table">
    <colgroup><col style="width:149px"><col style="width:100px"><col style="width:103px"><col style="width:96px"><col style="width:117px"><col style="width:122px"><col></colgroup>
    <tr><th>Spread-name</th><th>avg sprd</th><th>+ve prob</th><th>-ve prob</th><th>spike prob</th><th>avg supply</th><th>supply cut_prob</th></tr>
    <tr><td>Spread1</td><td>item1</td><td></td><td></td><td></td><td></td><td></td></tr>
    <tr><td>Spread2</td><td>item2</td><td></td><td></td><td></td><td></td><td></td></tr>
    <tr><td>Spread3</td><td>item3</td><td></td><td></td><td></td><td></td><td></td></tr>
    <tr><td>Spread4</td><td>item4</td><td></td><td></td><td></td><td></td><td></td></tr>
    <tr><td>Spread5</td><td>Item5</td><td></td><td></td><td></td><td></td><td></td></tr>
  </table>
</section>

<section class="chart-panel">
  <div class="chart-card bars">
    <svg width="395" height="175" viewBox="0 0 395 175" font-family="Open Sans, Arial, sans-serif">
      <g stroke="#d8d8d8" stroke-width="1">
        <line x1="35" y1="28" x2="370" y2="28"/><line x1="35" y1="48" x2="370" y2="48"/><line x1="35" y1="68" x2="370" y2="68"/>
        <line x1="35" y1="88" x2="370" y2="88"/><line x1="35" y1="109" x2="370" y2="109"/><line x1="35" y1="130" x2="370" y2="130"/>
        <line x1="75" y1="28" x2="75" y2="151"/><line x1="117" y1="28" x2="117" y2="151"/><line x1="160" y1="28" x2="160" y2="151"/>
        <line x1="203" y1="28" x2="203" y2="151"/><line x1="243" y1="28" x2="243" y2="151"/><line x1="285" y1="28" x2="285" y2="151"/>
        <line x1="328" y1="28" x2="328" y2="151"/><line x1="370" y1="28" x2="370" y2="151"/>
      </g>
      <g font-size="11" fill="#222" text-anchor="end">
        <text x="25" y="61">50</text><text x="25" y="82">40</text><text x="25" y="103">30</text><text x="25" y="124">20</text><text x="25" y="145">10</text>
      </g>
      <rect x="52" y="48" width="22" height="103" fill="var(--olive)"/>
      <rect x="75" y="68" width="21" height="83" fill="var(--orange)"/>
      <rect x="96" y="88" width="21" height="63" fill="var(--slate)"/>
      <rect x="139" y="109" width="21" height="42" fill="var(--olive)"/>
      <rect x="160" y="48" width="21" height="103" fill="var(--navy)"/>
      <rect x="181" y="68" width="22" height="83" fill="var(--purple)"/>
      <rect x="203" y="88" width="21" height="63" fill="var(--slate)"/>
      <rect x="243" y="131" width="21" height="20" fill="var(--brown)"/>
      <rect x="264" y="88" width="21" height="63" fill="var(--orange)"/>
      <rect x="285" y="68" width="22" height="83" fill="var(--navy)"/>
      <rect x="307" y="48" width="21" height="103" fill="var(--slate)"/>
      <rect x="328" y="109" width="21" height="42" fill="var(--purple)"/>
      <polyline points="35,22 35,151 378,151" fill="none" stroke="#222" stroke-width="1.5"/>
      <g font-size="10" fill="#222" text-anchor="middle">
        <text x="85" y="167">your text</text><text x="181" y="167">your text</text><text x="296" y="167">your text</text>
      </g>
    </svg>
  </div>
  <div class="chart-card pie">
    <svg width="396" height="178" viewBox="0 0 396 178" font-family="Open Sans, Arial, sans-serif">
      <path d="M211,75 L211,14 A61,61 0 0 1 263.8,44.5 Z" fill="var(--olive)"/>
      <path d="M211,75 L263.8,44.5 A61,61 0 0 1 176,125 Z" fill="var(--orange)"/>
      <path d="M211,75 L176,125 A61,61 0 0 1 158.2,44.5 Z" fill="var(--navy)"/>
      <path d="M211,75 L158.2,44.5 A61,61 0 0 1 211,14 Z" fill="var(--slate)"/>
      <g stroke="#fff" stroke-width="2">
        <line x1="170" y1="90" x2="150" y2="100"/><line x1="238" y1="108" x2="255" y2="122"/>
      </g>
      <g font-size="5" fill="#444">
        <text x="57" y="72">Weekly share</text><text x="57" y="79">of supply</text><text x="57" y="86">by hub</text>
        <text x="283" y="138">Spread volume</text><text x="283" y="145">split by</text><text x="283" y="152">region</text>
      </g>
      <text x="59" y="101" font-size="12" fill="#222">your text</text>
      <text x="284" y="128" font-size="12" fill="#222">your text</text>
    </svg>
  </div>
</section>

<footer class="footer"><span>Copyright © 2014</span><span class="brand-mini">Methara</span><span>All rights reserved</span></footer>
</body>
</html>
```